Bramblecrest Wellness Web Page

To create a web page that has the number 1 goal of converting Google Ad / Facebook Ads clicks into paying customers.
The site will feed into a web application where travellers can enter their trip and purchase a Roamwell Kit Guide.
The page / site needs to be able to tell people what we do and encourage them to start the process of getting a Roamwell Kit Guide.
It should be a wordpress theme.
Please see the attached brief for more information.

```html
<!DOCTYPE html>
<html lang="en">
<head>
<meta charset="utf-8">
<title>Bramblecrest Wellness</title>
<link href="https://fonts.googleapis.com/css2?family=Montserrat:wght@500;600;700&family=Arimo:wght@400;700&display=swap" rel="stylesheet">
<style>
:root{
  --navy:#1b2650;
  --blue:#3aa8cf;
  --blue-deep:#2f7aa6;
  --btn-a:#5aa7cf;
  --btn-b:#2c5f86;
  --ink:#1a1f3a;
  --muted:#8a8f98;
  --soft:#f3f4f4;
  --footer:#1e2a52;
  --white:#ffffff;
}
*{box-sizing:border-box;margin:0;padding:0}
html,body{width:1200px;height:4839px;overflow:hidden}
body{position:relative;background:var(--white);font-family:"Arimo",Arial,sans-serif;color:var(--ink)}
.abs{position:absolute}
.heading{font-family:"Montserrat",Arial,sans-serif;font-weight:700;color:var(--ink);line-height:1.25}
.accent{color:var(--blue)}
.btn{position:absolute;display:flex;align-items:center;justify-content:center;border-radius:24px;font-family:"Montserrat",Arial,sans-serif;font-weight:700;font-size:17px;color:var(--white);background:linear-gradient(90deg,var(--btn-a),var(--btn-b));white-space:nowrap}
.btn-outline{background:transparent;border:3px solid var(--white)}
.copy{font-size:13.5px;line-height:18px;color:#6f747c}

/* header */
.site-header{position:absolute;left:0;top:0;width:1200px;height:138px;background:var(--white);z-index:2}
.brand-disc{position:absolute;left:103px;top:0;width:140px;height:178px;background:var(--white);border-radius:0 0 70px 70px;z-index:3;display:flex;flex-direction:column;align-items:center;justify-content:center;padding-top:20px}
.brand-disc .dot{width:34px;height:34px;border-radius:50%;background:var(--blue-deep);margin-bottom:10px}
.brand-name{font-family:"Montserrat",Arial,sans-serif;font-weight:600;font-size:15px;color:var(--blue-deep);text-align:center;line-height:1.2}
.phone{position:absolute;right:290px;top:36px;font-family:"Montserrat",Arial,sans-serif;font-weight:600;font-size:18px;color:var(--blue);display:flex;align-items:center;gap:8px;white-space:nowrap}
.main-nav{position:absolute;top:91px;font-family:"Montserrat",Arial,sans-serif;font-weight:600;font-size:16px;color:#2e3550;white-space:nowrap}

/* hero */
.hero{position:absolute;left:0;top:138px;width:1200px;height:567px;background:linear-gradient(180deg,#9fb9c4 0%,#6d8a86 30%,#1f8f9c 55%,#12727f 80%,#cfd8dc 100%)}
.hero-title{position:absolute;left:0;width:1200px;top:118px;text-align:center;font-family:"Montserrat",Arial,sans-serif;font-weight:700;font-size:60px;color:var(--white)}

/* brief cards */
.brief{position:absolute;left:0;top:705px;width:1200px;height:636px;background:var(--soft)}
.section-title{position:absolute;left:0;width:1200px;text-align:center;font-size:40px}
.card{position:absolute;top:147px;width:296px;height:388px;background:var(--white)}
.card-img{height:200px;border-bottom:8px solid var(--blue)}
.card h3{position:absolute;left:26px;top:234px;font-family:"Montserrat",Arial,sans-serif;font-weight:600;font-size:20px;color:var(--ink)}
.card p{position:absolute;left:28px;top:270px;width:250px;font-size:13px;line-height:17px;color:var(--muted)}
.card .btn{left:26px;top:320px;width:128px;height:42px}

/* why buy */
.why-band{position:absolute;left:0;top:1867px;width:1200px;height:465px;background:var(--soft)}
.feature{position:absolute;top:2200px;width:297px;height:290px;background:var(--white);border:2px solid #8d9096;text-align:center}
.feature svg{position:absolute;left:108px;top:36px}
.feature h4{position:absolute;left:0;width:100%;top:155px;font-family:"Montserrat",Arial,sans-serif;font-weight:600;font-size:18px;color:var(--blue)}
.feature p{position:absolute;left:30px;width:233px;top:192px;font-size:13.5px;line-height:18px;color:#6f747c}

/* bands */
.vaccine-band{position:absolute;left:0;top:3075px;width:1200px;height:537px;background:var(--blue)}
.cta-band{position:absolute;left:0;top:4323px;width:1200px;height:132px;background:var(--blue)}
.site-footer{position:absolute;left:0;top:4455px;width:1200px;height:384px;background:var(--footer);color:var(--white)}
.footer-rule{position:absolute;top:0;width:1px;height:330px;background:#3a4670}
.footer-col h5{font-family:"Montserrat",Arial,sans-serif;font-weight:600;font-size:21px;color:var(--blue);margin-bottom:30px}
.footer-col li{list-style:none;font-size:14px;line-height:26px}
.contact-row{position:absolute;left:832px;display:flex;align-items:center;gap:18px;font-size:14px;line-height:19px}
.contact-icon{width:50px;height:50px;border-radius:50%;background:var(--blue);display:flex;align-items:center;justify-content:center;flex:none}
.bottom-bar{position:absolute;left:0;top:330px;width:1200px;height:54px;border-top:1px solid #3a4670}
.social{position:absolute;top:14px;width:32px;height:32px;border-radius:50%;background:var(--white)}
</style>
</head>
<body>

<header class="site-header">
  <div class="brand-disc"><span class="dot"></span><div class="brand-name">Bramblecrest Wellness</div></div>
  <div class="phone">
    <svg width="18" height="18" viewBox="0 0 24 24"><path fill="#3aa8cf" d="M6.6 10.8a15 15 0 0 0 6.6 6.6l2.2-2.2a1 1 0 0 1 1-.25 11.4 11.4 0 0 0 3.6.57 1 1 0 0 1 1 1V20a1 1 0 0 1-1 1A17 17 0 0 1 3 4a1 1 0 0 1 1-1h3.5a1 1 0 0 1 1 1c0 1.25.2 2.45.57 3.57a1 1 0 0 1-.25 1z"/></svg>
    Call Us: 555 014 2290
  </div>
  <a class="btn" style="left:939px;top:24px;width:134px;height:46px">Buy Now</a>
  <nav>
    <span class="main-nav" style="left:413px">Home</span>
    <span class="main-nav" style="left:514px">About Us</span>
    <span class="main-nav" style="left:643px">What is a Travel Health</span>
    <span class="main-nav" style="left:889px">Disease</span>
    <span class="main-nav" style="left:1005px">Country</span>
  </nav>
</header>

<section class="hero" role="img" aria-label="Two travellers with backpacks sitting by a turquoise mountain lake">
  <h1 class="hero-title">Bramblecrest Wellness</h1>
  <a class="btn btn-outline" style="left:535px;top:200px;width:130px;height:46px;background:linear-gradient(90deg,var(--btn-a),var(--btn-b))">Buy Now</a>
</section>

<section class="brief">
  <h2 class="heading section-title" style="top:60px">Roamwell <span class="accent">Kit Guide</span></h2>
  <article class="card" style="left:127px">
    <div class="card-img" role="img" aria-label="Pagoda reflected in an autumn lake" style="background:linear-gradient(180deg,#5b6f8a,#b5643f 55%,#3f5d6a)"></div>
    <h3>Travel Health Name</h3>
    <p>Lorem ipsum dolor sit amet, conse ctetur adipiscing elit, sed do</p>
    <a class="btn">Buy Now</a>
  </article>
  <article class="card" style="left:452px">
    <div class="card-img" role="img" aria-label="Swing under a palm tree on a sunset beach" style="background:linear-gradient(180deg,#3d4a3a,#d9a878 55%,#a0826a)"></div>
    <h3>Travel Health Name</h3>
    <p>Lorem ipsum dolor sit amet, conse ctetur adipiscing elit, sed do</p>
    <a class="btn">Buy Now</a>
  </article>
  <article class="card" style="left:777px">
    <div class="card-img" role="img" aria-label="Green alpine valley below snowy peaks" style="background:linear-gradient(180deg,#3f74b8,#8aa3b8 35%,#4e8a2e 70%,#2f5a22)"></div>
    <h3>Travel Health Name</h3>
    <p>Lorem ipsum dolor sit amet, conse ctetur adipiscing elit, sed do</p>
    <a class="btn">Buy Now</a>
  </article>
</section>

<section class="about">
  <div class="why-band"></div>
  <div class="abs" role="img" aria-label="Hikers celebrating on a cliff above a coastal fjord village" style="left:597px;top:1445px;width:603px;height:500px;background:linear-gradient(180deg,#a9c3d6 0%,#6f8ea3 35%,#3f6a7c 60%,#5a5a4a 100%)"></div>
  <h2 class="heading abs" style="left:127px;top:1475px;font-size:38px;width:440px">What is <span class="accent">Bramblecrest Wellness?</span></h2>
  <p class="copy abs" style="left:127px;top:1590px;width:410px">Lorem ipsum dolor sit amet, consectetur adipiscing elit, sedo eiusmod tempor incididunt ut labore et dolore magna aliqua. Quis ipsum suspendisse ultrices gravida. Risus commodo viverra maecenas accumsan lacus vel facilisis. r incididunt ut labore et dolore magna aliqua. Quis ipsum suspendisse ultrices gravida. Risus commodo viverra maecenas accums an lacus vel facilisis.</p>
  <a class="btn" style="left:127px;top:1748px;width:150px;height:47px">Read More</a>
</section>

<section class="why">
  <h2 class="heading section-title" style="top:2040px">Why buy a <span class="accent">Roamwell Kit Guide</span></h2>
  <p class="copy abs" style="left:290px;top:2116px;width:620px;text-align:center">Lorem ipsum dolor sit amet, consectetur adipiscing elit, sedo eiusmod tempor incididunt ut labore et dolore magna aliqua. Quis ipsum suspendisse ultrices gravida.</p>
  <div class="feature" style="left:127px">
    <svg width="80" height="80" viewBox="0 0 80 80" fill="none" stroke="#2f7aa6" stroke-width="3"><circle cx="40" cy="42" r="30"/><path d="M10 42h60M40 12c-12 14-12 46 0 60M40 12c12 14 12 46 0 60"/></svg>
    <h4>Lorem Ipsum</h4>
    <p>Lorem ipsum dolor sit amet, consectetur adipiscing elit, sedo eiusmod tempor incididun</p>
  </div>
  <div class="feature" style="left:452px">
    <svg width="80" height="80" viewBox="0 0 80 80" fill="none" stroke="#2f7aa6" stroke-width="3"><path d="M40 46 25 31a9 9 0 0 1 15-11 9 9 0 0 1 15 11z"/><path d="M36 30h8M40 26v8"/><path d="M8 40l14 26h12M72 40 58 66H46"/></svg>
    <h4>Lorem Ipsum</h4>
    <p>Lorem ipsum dolor sit amet, consectetur adipiscing elit, sedo eiusmod tempor incididun</p>
  </div>
  <div class="feature" style="left:777px">
    <svg width="80" height="80" viewBox="0 0 80 80" fill="none" stroke="#2f7aa6" stroke-width="3"><rect x="16" y="10" width="44" height="62" rx="3"/><path d="M24 30l4 4 7-8M24 46l4 4 7-8M24 62l4 4 7-8M40 32h12M40 48h12M40 64h12"/></svg>
    <h4>Lorem Ipsum</h4>
    <p>Lorem ipsum dolor sit amet, consectetur adipiscing elit, sedo eiusmod tempor incididun</p>
  </div>
</section>

<section class="inside">
  <div class="abs" style="left:190px;top:2700px;width:380px;display:flex;align-items:center;gap:18px">
    <span style="width:60px;height:60px;border-radius:50%;background:linear-gradient(135deg,var(--btn-a),var(--btn-b));flex:none"></span>
    <span style="font-family:'Montserrat',Arial,sans-serif;font-weight:700;font-size:30px;color:var(--blue-deep)">Bramblecrest Wellness</span>
  </div>
  <h2 class="heading abs" style="left:612px;top:2647px;font-size:38px">What is in a<br><span class="accent">Roamwell Kit Guide</span></h2>
  <p class="copy abs" style="left:612px;top:2753px;width:405px">Lorem ipsum dolor sit amet, consectetur adipiscing elit, sedo eiusmod tempor incididunt ut labore et dolore magna aliqua. Quis ipsum suspendisse ultrices gravida. Lorem ipsum dolor sit amet, consectetur adipiscing elit, sedo eiusmod tempor incididunt ut labore et dolore magna aliqua. Quis ipsum suspendisse ultrices gravida.</p>
  <a class="btn" style="left:612px;top:2878px;width:150px;height:47px">Read More</a>
</section>

<section class="vaccines">
  <div class="vaccine-band"></div>
  <div class="abs" role="img" aria-label="Traveller working on a laptop on a bridge in forested mountains" style="left:627px;top:3147px;width:470px;height:525px;border-radius:235px 235px 0 0;background:linear-gradient(180deg,#c9d3d8 0%,#7d8f95 35%,#3c4f45 65%,#2a3630 100%)"></div>
  <h2 class="heading abs" style="left:133px;top:3180px;font-size:40px;color:var(--white)">What vaccines do<br>I need for....</h2>
  <p class="abs" style="left:133px;top:3300px;width:400px;font-size:13.5px;line-height:18px;color:var(--white)">Lorem ipsum dolor sit amet, consectetur adipiscing elit, sedo eiusmod tempor incididunt ut labore et dolore magna aliqua. Quis ipsum suspendisse ultrices gravida. Lorem ipsum dolor sit amet, consectetur adipiscing elit, sedo eiusmod tempor incididunt ut labore et dolore magna aliqua. Quis ipsum suspendisse ultrices gravida.</p>
  <a class="btn btn-outline" style="left:135px;top:3435px;width:150px;height:46px">Buy Now</a>
</section>

<section class="antimalarials">
  <div class="abs" role="img" aria-label="Medicine vials and a syringe on a laboratory table" style="left:127px;top:3807px;width:506px;height:441px;background:linear-gradient(135deg,#2f3a4a 0%,#7f8e9c 40%,#c9d0d5 70%,#8f6b50 100%)"></div>
  <h2 class="heading abs" style="left:673px;top:3837px;font-size:38px">What antimalarials<br><span class="accent">do I need for...</span></h2>
  <p class="copy abs" style="left:673px;top:3950px;width:405px">Lorem ipsum dolor sit amet, consectetur adipiscing elit, sedo eiusmod tempor incididunt ut labore et dolore mag na aliqua. Quis ipsum suspendisse ultrices gravidaorem ipsum dolor sit amet, consectetur adipiscing elit, sedo eiusmod tempor incididunt ut labore et dolore magna aliqua. Quis ipsum suspendisse ultrices gravida.</p>
  <a class="btn" style="left:673px;top:4098px;width:150px;height:45px">Buy Now</a>
</section>

<section class="cta-band">
  <p class="abs" style="left:127px;top:52px;font-family:'Montserrat',Arial,sans-serif;font-weight:600;font-size:23px;color:var(--white);white-space:nowrap">Lorem ipsum dolor sit amet, consectetur adipiscing elit,</p>
  <a class="btn btn-outline" style="left:894px;top:45px;width:150px;height:46px">Buy Now</a>
</section>

<footer class="site-footer">
  <div class="abs" style="left:127px;top:70px;width:150px;text-align:center">
    <span style="display:inline-block;width:44px;height:44px;border-radius:50%;background:var(--blue);margin-bottom:14px"></span>
    <div style="font-family:'Montserrat',Arial,sans-serif;font-weight:600;font-size:21px;color:var(--blue);line-height:1.2">Bramblecrest Wellness</div>
  </div>
  <span class="footer-rule" style="left:320px"></span>
  <span class="footer-rule" style="left:527px"></span>
  <span class="footer-rule" style="left:750px"></span>
  <div class="footer-col abs" style="left:370px;top:70px">
    <h5>Nav</h5>
    <ul><li>Home</li><li>What is Health</li><li>Contact Us</li><li>About Us</li><li>Disease</li><li>Country</li></ul>
  </div>
  <div class="footer-col abs" style="left:602px;top:70px">
    <h5>Links</h5>
    <ul><li>Disclaimer</li><li>Privacy</li><li>Terms</li><li>Refund</li></ul>
  </div>
  <h5 class="abs" style="left:837px;top:68px;font-family:'Montserrat',Arial,sans-serif;font-weight:600;font-size:21px;color:var(--blue)">Contact Us</h5>
  <div class="contact-row" style="top:120px">
    <span class="contact-icon"><svg width="20" height="20" viewBox="0 0 24 24"><path fill="#fff" d="M12 2a7 7 0 0 0-7 7c0 5 7 13 7 13s7-8 7-13a7 7 0 0 0-7-7zm0 9.5A2.5 2.5 0 1 1 12 6.5a2.5 2.5 0 0 1 0 5z"/></svg></span>
    <span>Location Name<br>Fernhill 210 Lark Row (0458)</span>
  </div>
  <div class="contact-row" style="top:183px">
    <span class="contact-icon"><svg width="20" height="20" viewBox="0 0 24 24"><path fill="#fff" d="M6.6 10.8a15 15 0 0 0 6.6 6.6l2.2-2.2a1 1 0 0 1 1-.25 11.4 11.4 0 0 0 3.6.57 1 1 0 0 1 1 1V20a1 1 0 0 1-1 1A17 17 0 0 1 3 4a1 1 0 0 1 1-1h3.5a1 1 0 0 1 1 1c0 1.25.2 2.45.57 3.57a1 1 0 0 1-.25 1z"/></svg></span>
    <span>Phone:555.014.7731</span>
  </div>
  <div class="contact-row" style="top:246px">
    <span class="contact-icon"><svg width="20" height="20" viewBox="0 0 24 24"><path fill="#fff" d="M3 5h18v14H3zm2 2v.5l7 4.5 7-4.5V7l-7 4.5z"/></svg></span>
    <span>hello@bramblecrest.example</span>
  </div>
  <div class="bottom-bar">
    <span class="social" style="left:127px"></span>
    <span class="social" style="left:174px"></span>
    <span class="social" style="left:219px"></span>
    <span class="social" style="left:266px"></span>
    <p class="abs" style="right:127px;top:19px;font-size:13px">© 2023 All Rights Reserved.Terms &amp; Conditions Privacy Policy</p>
  </div>
</footer>

</body>
</html>
```